Anzeigengestaltung für IT-Dienstleister
Zielgruppe
IT Dienstleister, spezialisiert auf IT Sicherheit / Informationssicherheit und Datenschutz. Zielgruppe sind Firmenkunden im Klein und Mittelstand. Die Anzeige ist für die WRK Zeitschrift Titelthema ist Digitalisierung.
Adresse / Internetseite / Ausbildung von mir soll auch mit in der Anzeige eingetragen sein.
Aufgabenstellung
Die Anzeige sollte klar und auffallend sein,
Anzeigengroße 71 x 124 mm
Die Mitgelieferten Dateien sollten in der Anzeige eingebaut sein.

```html
<!DOCTYPE html>
<html lang="de">
<head>
<meta charset="utf-8">
<title>Anzeige IT-Sicherheit</title>
<link href="https://fonts.googleapis.com/css2?family=Roboto:wght@400;500;700&display=swap" rel="stylesheet">
<style>
  :root {
    --brand-blue: #2f8fd0;
    --bar-blue: #2a86c8;
    --panel-top: #3a9be0;
    --panel-bottom: #1f6fb8;
    --badge-navy: #2c3f8f;
    --cert-green: #2d9a4a;
    --logo-dark: #3a3a3a;
    --white: #ffffff;
  }
  html, body { margin: 0; padding: 0; overflow: hidden; background: #ffffff; }
  .ad {
    position: relative; width: 687px; height: 1200px; overflow: hidden;
    background: var(--white); font-family: "Roboto", Arial, sans-serif;
  }
  .topic-bar {
    position: absolute; left: 0; top: 0; width: 100%; height: 49px;
    background: var(--bar-blue); color: var(--white);
    font-size: 27px; font-weight: 500; line-height: 49px; text-align: center;
    letter-spacing: 0.3px;
  }
  .membership-badge {
    position: absolute; top: 72px; height: 105px; box-sizing: border-box;
    border: 4px solid var(--badge-navy); border-radius: 10px;
  }
  .membership-badge.mark { left: 30px; width: 109px; }
  .membership-badge.label { left: 148px; width: 209px; }
  .headline {
    position: absolute; left: 36px; top: 212px; margin: 0;
    color: var(--brand-blue); font-size: 56px; font-weight: 700; letter-spacing: -0.5px;
  }
  .subline {
    position: absolute; left: 36px; top: 285px; width: 620px; margin: 0;
    color: var(--brand-blue); font-size: 28px; line-height: 37px;
  }
  .hero-photo {
    position: absolute; left: 156px; top: 400px; width: 492px; height: 477px;
    border-radius: 40px;
    background: radial-gradient(ellipse at 55% 35%, #2b2b2b 0%, #555 35%, #d8b8b0 65%, #ffffff 90%);
  }
  .cert-badge {
    position: absolute; left: 487px; top: 750px; width: 141px; height: 200px;
    box-sizing: border-box; border: 3px solid var(--cert-green); border-radius: 6px;
    background: var(--white);
  }
  .cert-badge .band { height: 62px; background: var(--cert-green); }
  .cert-badge .seal {
    position: absolute; left: 14px; top: 72px; width: 113px; height: 113px;
    border-radius: 50%; background: var(--cert-green);
  }
  .consultant {
    position: absolute; left: 20px; top: 902px; margin: 0;
    color: var(--brand-blue); font-size: 21px; line-height: 27px;
  }
  .consultant .name { font-weight: 700; font-size: 22px; }
  .contact-panel {
    position: absolute; left: 0; top: 1000px; width: 390px; height: 180px;
    border-radius: 0 22px 22px 0;
    background: linear-gradient(180deg, var(--panel-top), var(--panel-bottom));
    color: var(--white); font-size: 24px; line-height: 28px;
    box-sizing: border-box; padding: 12px 0 0 20px;
  }
  .contact-panel p { margin: 0; }
  .brand {
    position: absolute; left: 442px; top: 1100px; display: flex; align-items: center; gap: 10px;
    color: var(--logo-dark); font-size: 34px; font-weight: 700;
  }
  .brand .square { width: 22px; height: 22px; background: var(--brand-blue); }
</style>
</head>
<body>
<div class="ad">
  <div class="topic-bar">IT-Sicherheit&nbsp; | IT-Service | Datenschutz</div>

  <div class="membership-badge mark" role="img" aria-label="Verbandsabzeichen"></div>
  <div class="membership-badge label" role="img" aria-label="Beraterabzeichen"></div>

  <h1 class="headline">Kann man so machen!</h1>
  <p class="subline">Wenn Sie sich aber nachhaltig um Ihre IT-Sicherheit kümmern wollen kommen Sie besser zu uns.</p>

  <div class="hero-photo" role="img" aria-label="Foto: Strauß, der den Kopf in den Sand steckt"></div>

  <div class="cert-badge" role="img" aria-label="Zertifizierungssiegel Datenschutz">
    <div class="band"></div>
    <div class="seal"></div>
  </div>

  <p class="consultant">
    <span class="name">Markus Weidner</span><br>
    Diplom Wirtschaftsinformatiker (FH)<br>
    ISMS Auditor nach ISO 27001
  </p>

  <div class="contact-panel">
    <p>Lindenweg 7</p>
    <p>94130 Ortenried</p>
    <p>+49 (0)170 555 01 23</p>
    <p>info@weidner-online.de</p>
    <p>www.cyber-schutz-ost.de</p>
  </div>

  <div class="brand"><span class="square"></span>ITWeidner</div>
</div>
</body>
</html>
```